New Business Card Design Project

I would like my card design to look exactly like the logo, design, layout, and print of the current attached file. The only change I would like made would be for the print to say THE KMW GROUP instead of THE HALLORAN GROUP. Basically, just replace his group name with my group name. I would also like the backgroud to be the same texture and color as the attached file. I love the dark blue lettering and house logo on the card.

I am completely open to the rest of the card design. I just want something clean and simple. Only basic contact info required on the card. Maybe just name: Kyle M Warrick and cell # 555.914.2087 and email kyle@orchidhomesagent.com

```html
<!DOCTYPE html>
<html lang="en">
<head>
<meta charset="utf-8">
<title>The KMW Group — Business Card</title>
<link rel="stylesheet" href="https://fonts.googleapis.com/css2?family=Montserrat:wght@300;400&family=Open+Sans:wght@400;700&display=swap">
<style>
  :root {
    --navy: #1c1b3f;
    --paper: #f4f4f3;
    --paper-shade: #e7e7e5;
    --ink-grey: #8a8a8c;
    --ghost: #dcdcdb;
    --stage: #2a2a2a;
    --white: #ffffff;
  }
  * { margin: 0; padding: 0; box-sizing: border-box; }
  html, body {
    width: 1200px; height: 900px; overflow: hidden;
    background: var(--stage);
  }
  .stage {
    width: 1200px; height: 900px;
    display: flex; flex-direction: column; align-items: center; justify-content: center;
    gap: 40px;
  }
  .card {
    position: relative;
    width: 680px; height: 389px;
    background: linear-gradient(160deg, var(--white) 0%, var(--paper) 55%, var(--paper-shade) 100%);
    overflow: hidden;
    box-shadow: 0 10px 30px rgba(0,0,0,0.45);
  }

  /* Front */
  .brand {
    position: absolute; left: 200px; top: 118px;
    display: flex; align-items: center; gap: 30px;
  }
  .brand-square {
    width: 120px; height: 120px; background: var(--navy);
  }
  .brand-name {
    font-family: "Montserrat", sans-serif; font-weight: 300;
    color: var(--navy);
    font-size: 34px; line-height: 1.12; letter-spacing: 0.32em;
  }

  /* Back */
  .title-band {
    position: absolute; left: 0; right: 0; top: 28px; height: 70px;
    background: var(--navy);
    color: var(--white);
    display: flex; flex-direction: column; align-items: flex-end; justify-content: center;
    padding-right: 34px;
    font-family: "Open Sans", sans-serif;
  }
  .person-name { font-weight: 700; font-size: 21px; letter-spacing: 0.02em; line-height: 1.15; }
  .person-role { font-weight: 400; font-size: 14px; line-height: 1.2; }
  .ghost-square {
    position: absolute; right: 120px; bottom: 70px;
    width: 170px; height: 170px; background: var(--ghost);
  }
  .contact {
    position: absolute; left: 34px; bottom: 30px;
    font-family: "Open Sans", sans-serif; font-size: 15px; line-height: 1.45;
    color: var(--ink-grey);
    list-style: none;
  }
  .contact-label { font-weight: 700; color: var(--navy); margin-right: 4px; }
</style>
</head>
<body>
<main class="stage">
  <section class="card card-front">
    <div class="brand">
      <div class="brand-square"></div>
      <div class="brand-name">THE<br>KMW<br>GROUP</div>
    </div>
  </section>

  <section class="card card-back">
    <div class="ghost-square"></div>
    <div class="title-band">
      <span class="person-name">KYLE M WARRICK</span>
      <span class="person-role">CEO/FOUNDER</span>
    </div>
    <ul class="contact">
      <li><span class="contact-label">Phone:</span>555.914.2087</li>
      <li><span class="contact-label">Email:</span>kyle@orchidhomesagent.com</li>
      <li><span class="contact-label">Web:</span>orchidhomesagent.com</li>
    </ul>
  </section>
</main>
</body>
</html>
```